Stationary & Business Cards
TRB Weddings & Events by Greta
You need to extend the project before designers can submit more proposals, right now it is locked. Thank you! :)
And we need business cards, stationary & envelopes.
They like a zen feel...cherry blossoms...birds...
Thank you for all of your submissions. The owners do not like the purple logo anymore and have completly changed it. We have uploaded a eps file for it. This project is guaranteed and we will be picking a winner. If you have time please submit new designs. Thank you.
Your eps file is an image please upload orignal Ai file.
-Thanks
Please upload ai or eps of your logo.

```html
<!DOCTYPE html>
<html lang="en">
<head>
<meta charset="utf-8">
<title>TRB Weddings &amp; Events by Greta — Stationery Set</title>
<link rel="stylesheet" href="https://fonts.googleapis.com/css2?family=Jost:wght@400;500&family=Lato:wght@400;700&display=swap">
<style>
  :root {
    --leaf: #9dcb3b;
    --leaf-soft: #c9e28f;
    --paper: #ffffff;
    --paper-tint: #f7faef;
    --ink: #3a3a3a;
    --edge: #d9dccf;
    --stage: #ffffff;
  }
  * { box-sizing: border-box; margin: 0; padding: 0; }
  html, body { width: 1200px; height: 1101px; overflow: hidden; background: var(--stage); }
  .set { position: relative; width: 1200px; height: 1101px; font-family: "Lato", sans-serif; color: var(--ink); }

  .sheet { position: absolute; background: var(--paper); border: 1px solid var(--edge); box-shadow: 0 1px 3px rgba(0,0,0,.12); overflow: hidden; }
  .flourish { position: absolute; inset: 0; background:
      radial-gradient(ellipse at 30% 40%, rgba(201,226,143,.22), transparent 60%),
      radial-gradient(ellipse at 75% 75%, rgba(201,226,143,.18), transparent 55%),
      var(--paper-tint); }

  .mark { position: absolute; background: var(--leaf); border-radius: 6px; display: flex; align-items: center; justify-content: center;
          font-family: "Jost", sans-serif; font-weight: 400; color: var(--paper); letter-spacing: 1px; }
  .mark--reverse { background: var(--paper); color: var(--leaf); }
  .tagline { position: absolute; font-family: "Jost", sans-serif; font-weight: 400; color: var(--ink); white-space: nowrap; }

  /* Letterhead */
  .letterhead { left: 36px; top: 36px; width: 798px; height: 1029px; }
  .letterhead .mark { left: 42px; top: 42px; width: 84px; height: 80px; font-size: 26px; }
  .letterhead .tagline { left: 40px; top: 132px; font-size: 15px; }
  .letterhead .contact { position: absolute; left: 444px; top: 118px; font-size: 13px; line-height: 19px; }
  .contact .web { color: var(--leaf); }

  /* Business card front */
  .card-front { left: 849px; top: 36px; width: 330px; height: 189px; }
  .card-front .band { position: absolute; left: 0; top: 0; width: 100%; height: 54px;
          background: linear-gradient(90deg, var(--leaf-soft), #dcecb8 50%, var(--leaf-soft)); }
  .card-front .flourish { top: 54px; }
  .card-front .mark { left: 20px; top: 72px; width: 60px; height: 58px; font-size: 19px; }
  .card-front .person { position: absolute; left: 140px; top: 72px; }
  .person .name { color: var(--leaf); font-size: 13px; }
  .person .role { font-size: 10px; margin-top: 2px; }
  .card-front .contact { position: absolute; left: 140px; top: 112px; font-size: 9px; line-height: 13px; }

  /* Business card back */
  .card-back { left: 849px; top: 240px; width: 330px; height: 180px; background: var(--leaf); border-color: var(--leaf); }
  .card-back .mark { left: 135px; top: 60px; width: 60px; height: 58px; font-size: 19px; }

  /* Envelope */
  .envelope { left: 450px; top: 570px; width: 729px; height: 465px; }
  .envelope .flap { position: absolute; left: 0; top: 0; }
  .envelope .flap-mark { left: 337px; top: 96px; width: 54px; height: 52px; font-size: 17px; }
  .envelope .return .mark { left: 39px; top: 172px; width: 84px; height: 80px; font-size: 26px; }
  .envelope .return .tagline { left: 36px; top: 262px; font-size: 15px; }
  .envelope .return .city { top: 286px; left: 52px; font-size: 14px; }
</style>
</head>
<body>
<main class="set">

  <section class="sheet letterhead" aria-label="Letterhead">
    <div class="flourish" role="img" aria-label="Faint swirling floral pattern across the page"></div>
    <div class="mark">TRB</div>
    <p class="tagline">Weddings &amp; Events by Greta</p>
    <address class="contact" style="font-style:normal">
      Laguna Vista, CA &nbsp;|&nbsp; 714-555-0182<br>
      greta@trbweddingsandevents.com<br>
      <span class="web">www.trbweddingsandevents.com</span>
    </address>
  </section>

  <section class="sheet card-front" aria-label="Business card front">
    <div class="band" role="img" aria-label="Green floral swirl pattern band"></div>
    <div class="flourish" role="img" aria-label="Faint swirling floral pattern"></div>
    <div class="mark">TRB</div>
    <div class="person">
      <p class="name">Greta Lindqvist</p>
      <p class="role">Event Consultant</p>
    </div>
    <address class="contact" style="font-style:normal">
      Laguna Vista, CA &nbsp;|&nbsp; 714-555-0182<br>
      greta@trbweddingsandevents.com<br>
      <span class="web">www.trbweddingsandevents.com</span>
    </address>
  </section>

  <section class="sheet card-back" aria-label="Business card back">
    <div class="mark mark--reverse">TRB</div>
  </section>

  <section class="sheet envelope" aria-label="Envelope">
    <div class="flourish" role="img" aria-label="Faint swirling floral pattern across the envelope"></div>
    <svg class="flap" width="729" height="180" viewBox="0 0 729 180">
      <polygon points="0,0 729,0 364,176" fill="var(--leaf)"/>
    </svg>
    <div class="mark mark--reverse flap-mark">TRB</div>
    <div class="return">
      <div class="mark">TRB</div>
      <p class="tagline">Weddings &amp; Events by Greta</p>
      <p class="tagline city">Laguna Vista, CA</p>
    </div>
  </section>

</main>
</body>
</html>
```